Web design required

1-We need a web design for existing company based in New Zealand
2-We build residential house and light commercial
3-We has in-house designer which allow us can provide interior design
4-We modeling project before site construction, which enable both client and construction team to visually analysis whole project,

Target Market(s)

middle class residential house market
Ref: http://www.brambleworthbuilders.co.nz/

Industry/Entity Type

Construction Company

Number of Pages Required

1 page

Font styles to use
Sans Serif
Other font styles liked:
• Such as : Central Gothic or similar which has more design taste

Colors

Designer to choose colors to be used in the design.

Requirements
Must have
• Front sheet, contact information, sample project

```html
<!DOCTYPE html>
<html lang="en">
<head>
<meta charset="utf-8">
<title>Halcyon Homes — Builders</title>
<link rel="stylesheet" href="https://fonts.googleapis.com/css2?family=Lato:wght@300;400;700;900&display=swap">
<style>
:root{
  --blue:#0a6cb8;
  --blue-deep:#075a9a;
  --blue-dark:#0b4f85;
  --navy:#1f2d3d;
  --grey-bg:#eeeeee;
  --text:#555a60;
  --muted:#9aa0a6;
  --white:#ffffff;
}
*{margin:0;padding:0;box-sizing:border-box}
html,body{width:1200px;height:1200px;overflow:hidden;background:#fff}
body{font-family:"Lato",Arial,sans-serif;color:var(--text);position:relative}
.page{position:absolute;left:375px;top:8px;width:450px;height:1188px;overflow:hidden;background:#fff}
.shapes{position:absolute;left:0;top:0;width:450px;height:1188px}
.t{position:absolute;white-space:nowrap;line-height:1.2}

.topbar{position:absolute;left:0;top:0;width:450px;height:10px;background:var(--navy)}
.topbar .phone{left:25px;top:2px;font-size:5px;color:#fff}
.topbar .phone b{font-weight:400;font-size:5.5px;margin-left:2px}
.topbar .connect{left:326px;top:2.5px;font-size:3.6px;color:#fff;font-weight:700}
.topbar .enquire{position:absolute;left:376px;top:0;width:52px;height:10px;background:var(--blue);color:#fff;font-size:3.6px;font-weight:700;text-align:center;line-height:10px}

.brand{left:26px;top:26px;font-size:9px;font-weight:900;color:#fff;letter-spacing:1.4px;display:flex;align-items:center;gap:3px}
.brand i{display:inline-block;width:8px;height:8px;border:1.5px solid #fff;border-radius:50%}
.nav{top:29px;font-size:3.8px;color:#fff;font-weight:700}
.nav.active{border-bottom:.8px solid #fff;padding-bottom:2px}
.hero-kicker{left:28px;top:156px;font-size:5px;color:#fff;letter-spacing:1.6px}
.hero-title{left:28px;top:163px;font-size:9.4px;color:#fff;font-weight:700}

.welcome-k{left:248px;top:249px;font-size:5px;color:#2a2f35;font-weight:700}
.welcome-h{left:248px;top:254px;font-size:8.6px;font-weight:400;color:var(--muted)}
.welcome-h b{color:var(--blue);font-weight:700}
.para{position:absolute;font-size:3.8px;line-height:1.75;white-space:normal}
.welcome-p{left:248px;top:274px;width:174px;color:var(--text)}
.welcome-p p+p{margin-top:4px}

.jump{font-size:3.6px;color:var(--muted)}

.services-h{left:33px;top:466px;font-size:8px;font-weight:700;color:#fff}
.services-h span{color:#1a1f24}
.services-p{left:34px;top:484px;width:86px;color:#e6f0fa}
.svc{position:absolute;width:70px;text-align:center;font-size:5px;color:#fff;font-weight:700;line-height:1.5;white-space:normal}

.projects-h{left:344px;top:723px;font-size:8px;font-weight:700;color:#fff}
.projects-h span{color:var(--blue)}
.tile-label{font-size:4px;color:#fff;font-weight:900}

.contact-h{left:0;width:450px;text-align:center;top:1003px;font-size:8px;font-weight:700;color:#fff}
.contact-h span{color:#0f1a26}
.col-h{top:1055px;font-size:5px;color:#fff}
.small{font-size:3px;color:#dce9f5}
.apply{position:absolute;left:130px;top:1091px;width:40px;height:9px;background:#fff;color:var(--blue);font-size:3px;text-align:center;line-height:9px}
.quote-phone{left:233px;top:1083px;font-size:8.4px;color:#fff}
.field{position:absolute;background:var(--blue-dark);border:.5px solid rgba(255,255,255,.2);font-size:2.8px;color:#cfe0f0;padding:2px 3px}
.send{position:absolute;left:394px;top:1127px;width:32px;height:9px;background:#fff;color:var(--blue);font-size:3px;text-align:center;line-height:9px}
.footer{position:absolute;left:0;top:1158px;width:450px;height:30px;background:var(--blue-dark);color:#cfe0f0;font-size:3.2px;text-align:center;line-height:30px}
</style>
</head>
<body>
<main class="page">
  <svg class="shapes" viewBox="0 0 450 1188" xmlns="http://www.w3.org/2000/svg">
    <defs>
      <linearGradient id="heroGrad" x1="0" y1="0" x2="0" y2="1">
        <stop offset="0" stop-color="#8ea3d6"/>
        <stop offset=".5" stop-color="#6b7690"/>
        <stop offset=".75" stop-color="#3f8f8c"/>
        <stop offset="1" stop-color="#4a4446"/>
      </linearGradient>
      <linearGradient id="patioGrad" x1="0" y1="0" x2="0" y2="1">
        <stop offset="0" stop-color="#4a4c55"/>
        <stop offset=".4" stop-color="#c98a3e"/>
        <stop offset=".65" stop-color="#7a6a4a"/>
        <stop offset="1" stop-color="#3f6a2e"/>
      </linearGradient>
      <linearGradient id="siteGrad" x1="0" y1="0" x2="1" y2="1">
        <stop offset="0" stop-color="#2a73b4"/>
        <stop offset="1" stop-color="#1d5d98"/>
      </linearGradient>
      <linearGradient id="tileGrad" x1="0" y1="0" x2="0" y2="1">
        <stop offset="0" stop-color="#3a86c4"/>
        <stop offset="1" stop-color="#1f67a8"/>
      </linearGradient>
    </defs>

    <!-- hero -->
    <rect role="img" aria-label="Photo: two-storey home with lit pool at dusk" x="0" y="10" width="450" height="203" fill="url(#heroGrad)"/>
    <rect x="202" y="10" width="188" height="203" fill="#ffffff" opacity=".08"/>
    <path d="M412 165 l-3 3 l3 3 M420 173 l3 3 l-3 3" stroke="#fff" stroke-width=".9" fill="none"/>
    <polygon points="225,202 237,209 237,222 225,229 213,222 213,209" fill="#fff"/>
    <path d="M222 214 l3 3 l3 -3" stroke="#9aa0a6" stroke-width=".7" fill="none"/>

    <!-- welcome photo -->
    <polygon role="img" aria-label="Photo: lit living room opening onto a deck and lawn" points="0,218 216,218 189,336 264,414 0,414" fill="url(#patioGrad)"/>

    <!-- services background -->
    <polygon points="0,414 264,414 310,458 450,422 450,682 0,682" fill="var(--grey-bg)"/>
    <polygon points="0,420 84,384 160,464 132,572 24,600 0,580" fill="var(--blue)"/>

    <!-- hex links -->
    <g fill="none" stroke="#c4c8cc" stroke-width=".7">
      <polygon points="418,380 427,385 427,395 418,400 409,395 409,385"/>
      <polygon points="31,634 40,639 40,649 31,654 22,649 22,639"/>
      <polygon points="418,940 427,945 427,955 418,960 409,955 409,945"/>
    </g>
    <g fill="none" stroke="#9aa0a6" stroke-width=".6">
      <path d="M416 389 l2 2 l2 -2"/><path d="M29 643 l2 2 l2 -2"/><path d="M416 949 l2 2 l2 -2"/>
    </g>

    <!-- service hexes -->
    <g role="img" aria-label="Photos: planning, modelling and site management" fill="url(#siteGrad)" opacity=".92">
      <polygon transform="rotate(15 238 518)" points="238,473 277,495 277,541 238,563 199,541 199,495"/>
      <polygon transform="rotate(15 323 541)" points="323,496 362,518 362,564 323,586 284,564 284,518"/>
      <polygon transform="rotate(15 261 602)" points="261,557 300,579 300,625 261,647 222,625 222,579"/>
    </g>

    <!-- projects backdrop -->
    <polygon role="img" aria-label="Photo: builders in hard hats on site" points="258,682 450,682 450,892 348,918 262,832 234,774" fill="#2d6fae"/>

    <!-- project tiles -->
    <g role="img" aria-label="Photos of completed projects" fill="url(#tileGrad)">
      <rect x="39" y="774" width="121" height="56"/>
      <rect x="165" y="774" width="121" height="56"/>
      <rect x="291" y="774" width="121" height="56"/>
      <rect x="39" y="836" width="121" height="56"/>
      <rect x="165" y="836" width="121" height="56"/>
      <rect x="291" y="836" width="121" height="56"/>
    </g>

    <!-- contact -->
    <rect x="0" y="980" width="450" height="178" fill="var(--blue)"/>
    <g fill="none" stroke="#fff" stroke-width=".5" opacity=".8">
      <circle cx="42" cy="1080" r="4"/><circle cx="42" cy="1093" r="4"/><circle cx="42" cy="1106" r="4"/>
      <path d="M42 1078 a1.3 1.3 0 1 1 .01 0 M42 1081.5 v1"/>
      <rect x="40" y="1091.8" width="4" height="2.6"/><path d="M40 1092 l2 1.4 l2 -1.4"/>
      <path d="M40.6 1104.6 q.5 2.4 2.8 2.8"/>
      <circle cx="236" cy="1104" r="4.5"/><circle cx="246" cy="1104" r="4.5"/><circle cx="256" cy="1104" r="4.5"/><circle cx="266" cy="1104" r="4.5"/>
    </g>
  </svg>

  <!-- top bar -->
  <div class="topbar">
    <span class="t phone">&#9990; PHONE <b>1300 000 000</b></span>
    <span class="t connect">CONNECT WITH US</span>
    <span class="enquire">&#9993; ENQUIRE ONLINE</span>
  </div>

  <!-- header -->
  <div class="t brand"><i></i>HALCYON</div>
  <span class="t nav active" style="left:294px">HOME</span>
  <span class="t nav" style="left:322px">SERVICES</span>
  <span class="t nav" style="left:354px">ABOUT</span>
  <span class="t nav" style="left:378px">PROJECTS</span>
  <span class="t nav" style="left:406px">CONTACT</span>
  <span class="t hero-kicker">CREATING AND RENOVATING</span>
  <h1 class="t hero-title">BEAUTIFUL AND UNUSUAL BUILDINGS</h1>

  <!-- welcome -->
  <span class="t welcome-k">WELCOME TO</span>
  <h2 class="t welcome-h"><b>HALCYON</b> HOMES</h2>
  <div class="para welcome-p">
    <p>Halcyon Homes is dedicated to creating and renovating beautiful and unusual buildings.</p>
    <p>Halcyon Homes works with you to take dream houses off the blueprints and into reality. We have the knowledge and expertise to customise homes to suit you – from unusual materials and designs to environmentally sensitive locations.</p>
  </div>
  <span class="t jump" style="left:376px;top:387px">OUR SERVICES</span>

  <!-- services -->
  <h2 class="t services-h"><span>OUR</span> SERVICES</h2>
  <p class="para services-p">We design and build family homes and light commercial spaces, with an in-house designer for interiors and full 3D models of every project before work on site begins.</p>
  <div class="svc" style="left:203px;top:511px">Preconstruction<br>Planning</div>
  <div class="svc" style="left:288px;top:534px">Construction<br>Modelling</div>
  <div class="svc" style="left:226px;top:595px">Full Project<br>Management</div>
  <span class="t jump" style="left:46px;top:641px">OUR PROJECTS</span>

  <!-- projects -->
  <h2 class="t projects-h"><span>OUR</span> PROJECTS</h2>
  <span class="t tile-label" style="left:43px;top:822px">KOWHAI PROJECT</span>
  <span class="t tile-label" style="left:169px;top:822px">WESTBROOK PROJECT</span>
  <span class="t tile-label" style="left:295px;top:822px">RIVERSIDE PROJECT - INTERIOR</span>
  <span class="t tile-label" style="left:43px;top:884px">RIVERSIDE PROJECT</span>
  <span class="t tile-label" style="left:169px;top:884px">ASHGROVE PROJECT</span>
  <span class="t tile-label" style="left:295px;top:884px">MILL RD PROJECT</span>
  <span class="t jump" style="left:382px;top:947px">CONACT US</span>

  <!-- contact -->
  <h2 class="t contact-h"><span>CONTACT</span> HALCYON</h2>
  <span class="t col-h" style="left:36px">HEAD OFFICE</span>
  <span class="t col-h" style="left:130px">EMPLOYMENT</span>
  <span class="t col-h" style="left:233px">GET A QUOTE</span>
  <span class="t col-h" style="left:331px">INQUIRIES</span>
  <span class="t small" style="left:52px;top:1078px">12 Harbour View Road, Auckland</span>
  <span class="t small" style="left:52px;top:1091px">hello@halcyonhomes.nz</span>
  <span class="t small" style="left:52px;top:1104px">09 300 4821</span>
  <p class="para small" style="left:130px;top:1074px;width:88px;line-height:1.4">To apply for a job with Halcyon Homes, please send a cover letter together with your CV.</p>
  <span class="apply">Apply For A Job</span>
  <p class="para small" style="left:233px;top:1074px;width:80px;line-height:1.4">To get a quote, call us or contact us via social media.</p>
  <span class="t quote-phone">09 300 4821</span>
  <p class="para small" style="left:331px;top:1074px;width:92px;line-height:1.4">For any inquiries, questions or recommendations, please fill in the following form.</p>
  <span class="field" style="left:332px;top:1088px;width:46px;height:9px">&#9823; Your Name *</span>
  <span class="field" style="left:380px;top:1088px;width:46px;height:9px">&#9823; Subject</span>
  <span class="field" style="left:332px;top:1099px;width:94px;height:9px">&#9993; Your Email Address *</span>
  <span class="field" style="left:332px;top:1110px;width:94px;height:28px">&#9998; Your Message</span>
  <span class="send">SEND</span>

  <footer class="footer">© 2017 BY HALCYON HOMES</footer>
</main>
</body>
</html>
```